CareVantRx business cards

We need a business card design that we could customize as needed for employees. We will need space for Name, Title, 1-2 phone numbers and email address.

We are a Pharmacy Benefits Management (PBM) company for hospice agencies and beginning a nationwide expansion. Attached is a vector file of our logo.

Cards can be single or double sided.

Industry/Entity Type

Business

```html
<!DOCTYPE html>
<html lang="en">
<head>
<meta charset="utf-8">
<title>CareVantRx Business Cards</title>
<link rel="stylesheet" href="https://fonts.googleapis.com/css2?family=Jost:wght@400;500&display=swap">
<style>
  :root {
    --backdrop: #2b2b2d;
    --card-blue-light: #4aa9c9;
    --card-blue: #2c8fbf;
    --card-blue-deep: #1c6b98;
    --card-white: #f4f4f2;
    --brand-green: #8a9b45;
    --brand-blue: #2f6a92;
    --ink: #333638;
    --ink-soft: #44484b;
    --rule: #6c8ea8;
  }
  * { margin: 0; padding: 0; box-sizing: border-box; }
  html, body {
    width: 1200px; height: 900px; overflow: hidden;
    background: var(--backdrop);
    font-family: "Jost", "Century Gothic", sans-serif;
  }
  .canvas { position: relative; width: 1200px; height: 900px; }

  .card {
    position: absolute;
    left: 354px;
    width: 487px;
    height: 271px;
    box-shadow: 0 6px 14px rgba(0,0,0,0.45);
  }

  .card-front {
    top: 157px;
    border-radius: 30px 0 30px 0;
    background: radial-gradient(ellipse at 55% 40%, var(--card-blue-light) 0%, var(--card-blue) 45%, var(--card-blue-deep) 100%);
    display: flex; align-items: center; justify-content: center;
  }
  .front-brand {
    display: flex; align-items: center; gap: 12px;
    color: #ffffff; font-size: 30px; font-weight: 400;
  }
  .front-brand .brand-square {
    width: 40px; height: 40px; border-radius: 6px; background: #ffffff; opacity: 0.9;
  }

  .card-back {
    top: 467px;
    border-radius: 0 30px 0 30px;
    background: var(--card-white);
  }
  .back-brand {
    position: absolute; left: 32px; top: 27px;
    display: flex; align-items: center; gap: 14px;
  }
  .back-brand .brand-square {
    width: 60px; height: 60px; border-radius: 7px; background: var(--brand-blue);
  }
  .back-brand .brand-name {
    font-size: 50px; font-weight: 400; color: var(--brand-green); letter-spacing: -0.5px; line-height: 1;
  }

  .holder { position: absolute; left: 106px; top: 128px; }
  .holder-name { font-size: 19px; font-weight: 400; color: var(--ink); letter-spacing: 0.5px; line-height: 1.2; }
  .holder-title { font-size: 13px; color: var(--ink-soft); margin-top: 2px; }

  .rule {
    position: absolute; left: 102px; right: 0; top: 184px;
    height: 1px; background: var(--rule);
  }

  .contacts {
    position: absolute; left: 106px; top: 203px;
    list-style: none; font-size: 13px; color: var(--ink); line-height: 16px;
  }
  .contacts .label { display: inline-block; width: 20px; color: var(--brand-blue); }
</style>
</head>
<body>
<main class="canvas">
  <section class="card card-front" aria-label="Card front">
    <div class="front-brand">
      <span class="brand-square"></span>
      <span class="brand-name">CareVantRx</span>
    </div>
  </section>

  <section class="card card-back" aria-label="Card back">
    <div class="back-brand">
      <span class="brand-square"></span>
      <span class="brand-name">CareVantRx</span>
    </div>
    <div class="holder">
      <p class="holder-name">DANA WHITFIELD</p>
      <p class="holder-title">Operation Manager</p>
    </div>
    <div class="rule"></div>
    <ul class="contacts">
      <li><span class="label">T</span>(221) 33 512 40 18</li>
      <li><span class="label">M</span>(221) 77 604 13 82</li>
      <li><span class="label">E</span>dana@carevantrx.com</li>
    </ul>
  </section>
</main>
</body>
</html>
```